Business card on Pvc transparent frosted

I need a business advertising card that will be eye catching and fun.
Target Market(s)
Rednecks, country, hunters, Fisherman, ATV users, lifted trucks, cowboys, cattle ranchers, farmers, etc
Industry/Entity Type
Apparel Store
Contact Information for Business Card
This will he printed on single side of a transparent frosted plastic card with shinny foil print option.
Requirements
Must have
- 1 - My logo.
- 2 - HOLLER BOOTSTRAP OUTFITTERS
- 3 - my motto "DONT judge how we look..... Judge the WILD mess we make!!"; 4 - my website "hollerbootstrap@mailvex.example"

Nice to have
- Use your imagination with negative space, partial graffics, etc. Keep in mind you can kind of see through the card

Should not have
- Do not change colors of chevrons

```html
<!DOCTYPE html>
<html lang="en">
<head>
<meta charset="utf-8">
<title>Holler Bootstrap Outfitters – Business Card</title>
<link rel="stylesheet" href="https://fonts.googleapis.com/css2?family=Josefin+Sans:wght@400;600&family=Metal+Mania&display=swap">
<style>
  :root {
    --backdrop: #e4e4e4;
    --card-black: #121212;
    --facet-light: #262626;
    --facet-dark: #0a0a0a;
    --foil-yellow: #f6d03a;
    --ember-red: #e0261f;
    --ink-white: #f4f4f4;
    --divider-grey: #3a3a3a;
  }
  * { margin: 0; padding: 0; box-sizing: border-box; }
  html, body {
    width: 1200px;
    height: 1000px;
    overflow: hidden;
    background: var(--backdrop);
  }
  .canvas {
    position: relative;
    width: 1200px;
    height: 1000px;
  }
  .business-card {
    position: absolute;
    left: 310px;
    top: 60px;
    width: 580px;
    height: 880px;
    background: var(--card-black);
    overflow: hidden;
    box-shadow: 0 6px 18px rgba(0,0,0,0.18);
  }
  .faceted-backdrop {
    position: absolute;
    inset: 0;
    background: linear-gradient(135deg, var(--facet-light) 0%, var(--facet-dark) 40%, #1b1b1b 60%, var(--facet-dark) 100%);
  }
  .brand-mark {
    position: absolute;
    top: 120px;
    left: 0;
    right: 0;
    display: flex;
    flex-direction: column;
    align-items: center;
    gap: 28px;
  }
  .brand-mark__square {
    width: 120px;
    height: 120px;
    background: var(--ember-red);
  }
  .brand-mark__name {
    font-family: "Josefin Sans", sans-serif;
    font-weight: 600;
    font-size: 58px;
    line-height: 62px;
    letter-spacing: 2px;
    text-align: center;
    color: var(--ink-white);
  }
  .motto {
    position: absolute;
    top: 445px;
    left: 40px;
    right: 40px;
    text-align: center;
    font-family: "Josefin Sans", sans-serif;
    font-weight: 400;
    font-size: 18px;
    line-height: 27px;
    color: var(--ink-white);
    letter-spacing: 0.5px;
  }
  .divider {
    position: absolute;
    top: 525px;
    left: 50%;
    width: 80px;
    height: 2px;
    margin-left: -40px;
    background: var(--divider-grey);
  }
  .store-title {
    position: absolute;
    top: 560px;
    left: 0;
    right: 0;
    text-align: center;
    font-family: "Metal Mania", cursive;
    font-weight: 400;
    font-size: 34px;
    color: var(--foil-yellow);
    text-shadow: 2px 2px 0 var(--ember-red);
    letter-spacing: 0.5px;
  }
  .contact-icons {
    position: absolute;
    top: 655px;
    left: 0;
    right: 0;
    display: flex;
    justify-content: center;
    gap: 60px;
  }
  .contact-icon { width: 46px; height: 46px; }
  .contact-lines {
    position: absolute;
    top: 735px;
    left: 0;
    right: 0;
    text-align: center;
    font-family: "Josefin Sans", sans-serif;
    font-size: 22px;
    color: var(--ink-white);
    letter-spacing: 1px;
    line-height: 44px;
  }
  .contact-lines .accent { color: var(--ember-red); }
</style>
</head>
<body>
<main class="canvas">
  <article class="business-card">
    <div class="faceted-backdrop" role="img" aria-label="Dark low-poly faceted background texture"></div>

    <div class="brand-mark">
      <span class="brand-mark__square"></span>
      <span class="brand-mark__name">HOLLER<br>BOOTSTRAP</span>
    </div>

    <p class="motto">DONT judge how we look.....<br>Judge the WILD mess we make!!</p>

    <div class="divider"></div>

    <h1 class="store-title">HOLLER BOOTSTRAP OUTFITTERS</h1>

    <div class="contact-icons">
      <svg class="contact-icon" viewBox="0 0 46 46" aria-label="Website">
        <circle cx="23" cy="23" r="21" fill="var(--foil-yellow)" stroke="var(--ember-red)" stroke-width="3"/>
        <g fill="none" stroke="var(--ember-red)" stroke-width="1.8">
          <circle cx="23" cy="23" r="11"/>
          <ellipse cx="23" cy="23" rx="5" ry="11"/>
          <line x1="12" y1="23" x2="34" y2="23"/>
          <line x1="14" y1="17" x2="32" y2="17"/>
          <line x1="14" y1="29" x2="32" y2="29"/>
        </g>
      </svg>
      <svg class="contact-icon" viewBox="0 0 46 46" aria-label="Email">
        <circle cx="23" cy="23" r="21" fill="var(--foil-yellow)" stroke="var(--ember-red)" stroke-width="3"/>
        <rect x="12" y="15" width="22" height="16" fill="var(--ember-red)"/>
        <polyline points="12,15 23,25 34,15" fill="none" stroke="var(--foil-yellow)" stroke-width="1.8"/>
      </svg>
    </div>

    <div class="contact-lines">
      <p>www.hollerbootstrap.example</p>
      <p>hollerbootstrap<span class="accent">@mailvex</span>.example</p>
    </div>
  </article>
</main>
</body>
</html>
```